4 page brochure for Logistics Company

Need a 4 page brochure (ie folded A3) for a Logistics company.
Service is a virtual network of warehouse and logistics companies.
Style is professional but accessible.
We have logo and styles designed and will upload these.
We have identified example images that could be used in the brochure.
Content will be uploaded also.
Updates
Reason: A couple of designers requested more time
Am giving another 24 hours to finalise and will then select most suitable design
Target Market(s)
40 to 60 year old business owners (traditional) - Australian
Industry/Entity Type
It Company
Requirements
Must have
- Professional
Should not have
- Nothing tacky

```html
<!DOCTYPE html>
<html lang="en">
<head>
<meta charset="utf-8">
<title>Meridian Freight Alliance – Brochure</title>
<link href="https://fonts.googleapis.com/css2?family=Didact+Gothic&family=Cinzel:wght@500&display=swap" rel="stylesheet">
<style>
:root{
  --navy:#173f78;
  --navy-dark:#0f2c57;
  --blue:#2560a8;
  --blue-light:#5b8fcf;
  --green:#8cc63f;
  --ink:#2b2f36;
  --grey:#6d737b;
  --rule:#c9ced6;
  --paper:#ffffff;
  --backdrop:#e6e7e9;
  --warm:#d9b35a;
}
*{box-sizing:border-box;margin:0;padding:0}
html,body{width:1200px;height:2510px;overflow:hidden}
body{background:var(--backdrop);font-family:"Didact Gothic",Arial,sans-serif;color:var(--ink);position:relative}
.page{position:absolute;background:var(--paper);overflow:hidden;box-shadow:0 4px 14px rgba(0,0,0,.18)}
.cover{left:320px;top:37px;width:560px;height:792px}
.spread{left:50px;top:866px;width:1100px;height:778px;display:flex}
.back{left:320px;top:1681px;width:560px;height:792px}
.abs{position:absolute}
svg.fill{position:absolute;left:0;top:0}

/* cover */
.brand{position:absolute;left:40px;top:34px;display:flex;align-items:center;gap:10px;color:var(--navy)}
.brand-mark{width:26px;height:26px;background:var(--navy)}
.brand-name{font-size:40px;letter-spacing:1px}
.brand-full{font-size:11px;line-height:12px;text-transform:uppercase;letter-spacing:1px;color:var(--grey)}
.tagline{position:absolute;left:250px;top:588px;width:300px;font-size:16px;line-height:19px;color:var(--navy);transform:rotate(-14deg);text-align:right}
.cover-title{position:absolute;left:36px;top:714px;font-family:"Cinzel",Georgia,serif;font-size:24px;color:#fff;transform:rotate(-9deg);transform-origin:left;letter-spacing:1px}

/* spread */
.half{position:relative;width:550px;height:778px;overflow:hidden}
.half.left{border-right:1px solid #dde1e6}
.intro{position:absolute;font-size:12px;line-height:15px;text-align:center;color:var(--grey)}
.intro b{color:var(--navy)}
.bar{position:absolute;height:20px;background:linear-gradient(90deg,var(--navy),var(--blue-light));color:#fff;font-size:12px;line-height:20px;padding-left:10px;font-weight:bold}
.h-blue{position:absolute;color:var(--navy);font-size:13px;line-height:15px;font-weight:bold}
.txt{position:absolute;font-size:8.5px;line-height:11px;color:var(--ink)}
.row{position:absolute;display:flex;gap:8px;font-size:8px;line-height:10px}
.row .lbl{width:62px;flex:none;font-weight:bold;color:var(--navy)}
.row ul{list-style:none}
.row li::before{content:"› ";color:var(--blue)}
.photo{position:absolute;background:linear-gradient(135deg,#c58a3c,#e9d28a 45%,#8f8577)}
.photo.cool{background:linear-gradient(160deg,#d8dde4,#9ea9b6 55%,#5e6b7a)}
.person{position:absolute;background:linear-gradient(#b9c0c9,#7d8794);border:1px solid var(--rule)}
table.grid{position:absolute;border-collapse:collapse;font-size:7.5px;line-height:9px}
table.grid th{background:var(--navy);color:#fff;padding:4px 5px;font-weight:normal;border:1px solid #fff}
table.grid td{border:1px solid var(--rule);padding:4px 5px;vertical-align:top}
table.grid td.side{background:linear-gradient(90deg,var(--navy),var(--blue));color:#fff;font-weight:bold;width:56px}
.terms{position:absolute;left:38px;top:440px;width:380px}
.terms .row{position:relative;margin-bottom:7px}
.hex{position:absolute;width:44px;height:44px;background:var(--navy);clip-path:polygon(25% 5%,75% 5%,100% 50%,75% 95%,25% 95%,0 50%)}
.contact{position:absolute;font-size:9px;line-height:13px;color:var(--ink);text-align:center}
</style>
</head>
<body>

<!-- Front cover -->
<section class="page cover">
  <svg class="fill" width="560" height="792" viewBox="0 0 560 792">
    <defs>
      <linearGradient id="coverBg" x1="0" y1="0" x2="1" y2="1">
        <stop offset="0" stop-color="#ffffff"/><stop offset="1" stop-color="#d9dde2"/>
      </linearGradient>
      <linearGradient id="warehouseTone" x1="0" y1="0" x2="1" y2="1">
        <stop offset="0" stop-color="#e9d59a"/><stop offset=".45" stop-color="#c79a4a"/><stop offset="1" stop-color="#7a7464"/>
      </linearGradient>
      <linearGradient id="navyBand" x1="0" y1="0" x2="1" y2="0">
        <stop offset="0" stop-color="#0f2c57"/><stop offset="1" stop-color="#2560a8"/>
      </linearGradient>
    </defs>
    <rect width="560" height="792" fill="url(#coverBg)"/>
    <path d="M0 180 Q60 160 92 140 Q70 430 40 720 L0 740 Z" fill="url(#navyBand)"/>
    <path d="M92 140 Q300 118 560 95 L560 520 Q300 600 40 720 Q70 430 92 140 Z" fill="url(#warehouseTone)" role="img" aria-label="Photo of a large warehouse with tall pallet racking and a forklift"/>
    <path d="M40 720 Q300 600 560 520 L560 540 Q300 622 34 742 Z" fill="#8cc63f"/>
    <path d="M0 740 Q250 680 560 625 L560 685 Q250 730 0 792 Z" fill="url(#navyBand)"/>
  </svg>
  <div class="brand">
    <div class="brand-mark"></div>
    <div class="brand-name">MFA</div>
    <div class="brand-full">Meridian<br>Freight<br>Alliance</div>
  </div>
  <p class="tagline">A new solution for Australian<br>warehouse business owners</p>
  <p class="cover-title">Scale : Synergy : Value</p>
</section>

<!-- Inside spread -->
<section class="page spread">
  <div class="half left">
    <svg class="fill" width="550" height="778" viewBox="0 0 550 778">
      <defs>
        <linearGradient id="sideFade" x1="0" x2="1"><stop offset="0" stop-color="#2560a8"/><stop offset="1" stop-color="#ffffff" stop-opacity="0"/></linearGradient>
      </defs>
      <rect width="26" height="778" fill="url(#sideFade)" opacity=".6"/>
      <path d="M0 720 Q250 690 550 700 L550 778 L0 778 Z" fill="#173f78"/>
      <path d="M0 712 Q250 682 550 692 L550 700 Q250 690 0 720 Z" fill="#5b8fcf"/>
    </svg>
    <p class="intro" style="left:110px;top:22px;width:340px">Offering national <b>scale</b> to increase revenues, achieving <b>synergies</b> to reduce costs, and enhancing the <b>value</b> in your business.</p>
    <div class="bar" style="left:26px;top:74px;width:250px">The challenges (Why?)</div>
    <p class="txt" style="left:40px;top:100px;width:240px">Australian warehouse business owners are facing unprecedented challenges to diversify their client base, compete for work with national clients, and enhance their profitability and, ultimately, their business.</p>
    <div class="photo cool" style="left:40px;top:146px;width:110px;height:70px" role="img" aria-label="Photo of a long warehouse aisle with racking"></div>
    <p class="h-blue" style="left:290px;top:98px;width:240px;font-size:11px">Australian warehouse industry dynamics</p>
    <ul class="txt" style="left:300px;top:116px;width:130px;list-style:none">
      <li>› Highly fragmented – 4,000 businesses across the country</li>
      <li>› Single-site operators – increasing challenge to compete</li>
      <li>› Accelerating consolidation</li>
      <li>› Margin pressure – profits falling</li>
      <li>› High customer concentration</li>
      <li>› Ongoing need to invest in technology</li>
    </ul>
    <svg class="abs" style="left:440px;top:118px" width="96" height="64" viewBox="0 0 96 64">
      <rect x=".5" y=".5" width="95" height="63" fill="#fff" stroke="#c9ced6"/>
      <text x="48" y="10" font-size="6" text-anchor="middle" fill="#2b2f36" font-family="Didact Gothic, sans-serif">Gross profit margin</text>
      <line x1="10" y1="56" x2="90" y2="56" stroke="#c9ced6"/>
      <line x1="10" y1="14" x2="10" y2="56" stroke="#c9ced6"/>
      <polyline points="12,20 28,26 44,30 60,38 76,44 88,50" fill="none" stroke="#2560a8" stroke-width="1.5"/>
    </svg>
    <div class="photo" style="left:330px;top:248px;width:120px;height:66px;background:linear-gradient(135deg,#f1e9d2,#d8c99a)" role="img" aria-label="Map of Australia showing member warehouse locations"></div>
    <p class="h-blue" style="left:40px;top:232px;width:220px">Warehouse owners have a challenge to exit their business</p>
    <div class="row" style="left:40px;top:268px;width:250px"><span class="lbl">Lack of sellers</span><ul><li>Few buyers for single-site operators</li><li>Owners nearing retirement age</li></ul></div>
    <div class="row" style="left:40px;top:300px;width:250px"><span class="lbl">Inability to attract buyers</span><ul><li>Many single-site operators lack the size to attract a corporate buyer</li><li>Succession through family is not an option</li><li>Reliance on the owner operator</li></ul></div>
    <div class="row" style="left:40px;top:352px;width:250px"><span class="lbl">Need to cash out</span><ul><li>Capital costs need to be recovered</li><li>Long leases carry exit penalties</li><li>Need to fund retirement</li></ul></div>
    <div class="bar" style="left:300px;top:322px;width:250px">The solution (What?)</div>
    <p class="txt" style="left:300px;top:348px;width:230px">The alliance provides a national platform to deliver scale to its members. Through this scale, the alliance and its members will secure new business. The value of members' businesses will increase, and members will be presented with multiple options to exit.</p>
    <p class="h-blue" style="left:40px;top:400px;width:240px">The alliance delivers scale, synergies, value and potential exit to its membership</p>
    <div class="row" style="left:40px;top:446px;width:250px"><span class="lbl">Scale</span><ul><li>By leveraging its membership and national presence, the alliance will present as a premium logistics provider to large national clients</li><li>Total scale at launch is expected to exceed 100,000 m² of warehouse space</li></ul></div>
    <div class="row" style="left:40px;top:500px;width:250px"><span class="lbl">Synergy</span><ul><li>The alliance will provide a centralised business development function</li><li>Joint buying will reduce costs to members</li></ul></div>
    <div class="row" style="left:300px;top:424px;width:240px"><span class="lbl">Value</span><ul><li>Members' businesses will increase in value as new work is transferred</li><li>Higher multiples and value than any individual member could achieve</li></ul></div>
    <div class="row" style="left:300px;top:478px;width:240px"><span class="lbl">Potential Exit</span><ul><li>For members who wish to sell some or all of their business, the alliance will offer to acquire part of their business</li><li>Members can remain as long as they choose</li></ul></div>
  </div>

  <div class="half right">
    <svg class="fill" width="550" height="778" viewBox="0 0 550 778">
      <defs>
        <linearGradient id="sideFadeR" x1="1" x2="0"><stop offset="0" stop-color="#2560a8"/><stop offset="1" stop-color="#ffffff" stop-opacity="0"/></linearGradient>
      </defs>
      <rect x="524" width="26" height="778" fill="url(#sideFadeR)" opacity=".6"/>
      <path d="M0 700 Q300 690 550 720 L550 778 L0 778 Z" fill="#173f78"/>
      <path d="M0 692 Q300 682 550 712 L550 720 Q300 690 0 700 Z" fill="#5b8fcf"/>
    </svg>
    <p class="intro" style="left:150px;top:22px;width:360px;text-align:right">The alliance's unique approach enables business owners to join with national scale, at low cost, while retaining control of their business. The approach is focused on achieving maximum value for the business owner over 3 phases.</p>
    <div class="bar" style="left:0;top:74px;width:250px">The approach (How?)</div>
    <p class="h-blue" style="left:38px;top:102px;font-size:14px">The alliance journey involves 3 phases</p>
    <table class="grid" style="left:38px;top:124px;width:440px">
      <tr><td class="side">Phase</td><th>Phase 1 – National Platform</th><th>Phase 2 – Roll up</th><th>Phase 3 – Exit</th></tr>
      <tr><td class="side">Activity</td><td>Form national alliance and win new contracts</td><td>Merge and integrate member operations</td><td>Scale business for listing or trade sale</td></tr>
      <tr><td class="side">Outcomes</td><td>Increased revenues and utilisation for members</td><td>Greater efficiency and value uplift</td><td>Liquidity for owners at higher multiples</td></tr>
    </table>
    <p class="h-blue" style="left:38px;top:416px;font-size:14px">Key membership terms</p>
    <div class="terms">
      <div class="row"><span class="lbl">Fee Structure</span><ul><li>Membership is primarily success based</li><li>Low cost annual fee</li></ul></div>
      <div class="row"><span class="lbl">Alignment</span><ul><li>Standard levels of service must be adopted to secure national accounts</li></ul></div>
      <div class="row"><span class="lbl">Exit</span><ul><li>A pre-agreed process for valuing member businesses will be applied at entry to Phase 2</li></ul></div>
      <div class="row"><span class="lbl">Exclusivity</span><ul><li>Members will be offered a degree of exclusivity based on geography and service</li></ul></div>
      <div class="row"><span class="lbl">Complete Flexibility</span><ul><li>Members have no obligation to progress to Phase 2</li></ul></div>
    </div>
    <div class="hex" style="left:468px;top:440px"></div>
    <div class="hex" style="left:468px;top:494px"></div>
    <p class="h-blue" style="left:300px;top:588px;font-size:14px">Our objectives (Benefits)</p>
    <p class="txt" style="left:38px;top:610px;width:470px;font-size:9px;line-height:12px">The alliance intends to deliver tangible benefits to its members resulting in improved profitability, reduced risk and the achievement of measurably higher value. As such, the alliance offers significant benefits and clear strategic advantages, while presenting a flexible approach with few obligations on members at entry.</p>
  </div>
</section>

<!-- Back page -->
<section class="page back">
  <svg class="fill" width="560" height="792" viewBox="0 0 560 792">
    <defs>
      <linearGradient id="backNavy" x1="0" x2="1"><stop offset="0" stop-color="#0f2c57"/><stop offset="1" stop-color="#2560a8"/></linearGradient>
    </defs>
    <path d="M0 0 H560 V30 Q300 50 0 20 Z" fill="#eef1f5"/>
    <path d="M0 735 Q280 700 560 715 L560 792 L0 792 Z" fill="url(#backNavy)"/>
    <path d="M0 727 Q280 692 560 707 L560 715 Q280 700 0 735 Z" fill="#8cc63f"/>
  </svg>
  <p class="h-blue" style="left:30px;top:34px;font-size:11px">Tangible benefits of membership</p>
  <svg class="abs" style="left:30px;top:52px" width="220" height="120" viewBox="0 0 220 120">
    <rect x=".5" y=".5" width="219" height="119" fill="#fff" stroke="#c9ced6"/>
    <text x="110" y="12" font-size="7" text-anchor="middle" fill="#2b2f36" font-family="Didact Gothic, sans-serif">Indicative member outcomes</text>
    <line x1="20" y1="104" x2="210" y2="104" stroke="#c9ced6"/>
    <line x1="20" y1="20" x2="20" y2="104" stroke="#c9ced6"/>
    <rect x="40" y="80" width="24" height="24" fill="#9ea9b6"/>
    <rect x="82" y="64" width="24" height="40" fill="#5b8fcf"/>
    <rect x="124" y="44" width="24" height="60" fill="#2560a8"/>
    <rect x="166" y="28" width="24" height="76" fill="#173f78"/>
  </svg>
  <p class="txt" style="left:30px;top:180px;width:220px;font-size:7.5px">Indicative value improvement achieved by members</p>
  <div class="photo cool" style="left:30px;top:194px;width:220px;height:110px" role="img" aria-label="Photo of warehouse racking stocked with pallets"></div>
  <table class="grid" style="left:262px;top:34px;width:272px">
    <tr><th style="background:#fff;border:none"></th><th>Outcome</th><th>Approach</th></tr>
    <tr><td class="side">Profitable Improvement</td><td>Increased revenue and utilisation</td><td>National sales function and shared client base</td></tr>
    <tr><td class="side">Reduced Risk</td><td>Diversified clients and lower costs</td><td>Joint buying, shared systems and scale</td></tr>
    <tr><td class="side">Measurable Value</td><td>Higher valuation of member business</td><td>Clear pathway to exit at higher multiples</td></tr>
  </table>
  <p class="txt" style="left:170px;top:320px;width:360px;text-align:right;font-size:9px;line-height:12px">With over 30 years of experience in warehouse, logistics and transportation and over 20 years of history in mergers, acquisitions and business sales, the team is uniquely qualified to deliver outcomes for its members.</p>
  <div class="bar" style="left:0;top:368px;width:260px">Our team (Who?)</div>
  <div class="abs" style="left:70px;top:392px;width:200px;background:var(--navy);color:#fff;font-size:9px;text-align:center;padding:2px">Meridian Freight Alliance</div>
  <ul class="txt" style="left:24px;top:418px;width:120px;list-style:none;font-size:7.5px;line-height:10px">
    <li><b>› Logistics industry expertise</b></li><li>Decades of operating experience</li>
    <li><b>› Credibility with clients</b></li><li>Long relationships with national shippers</li>
    <li><b>› M&amp;A and advisory expertise</b></li><li>Completed transactions across the sector</li>
    <li><b>› Breadth of expertise</b></li><li>Operations, finance, strategy and technology</li>
  </ul>
  <p class="txt" style="left:150px;top:418px;font-weight:bold;color:var(--navy)">Graham Pell</p>
  <div class="person" style="left:150px;top:432px;width:34px;height:40px" role="img" aria-label="Portrait of Graham Pell"></div>
  <ul class="txt" style="left:190px;top:432px;width:100px;list-style:none;font-size:7px;line-height:9px"><li>› Former logistics executive</li><li>› Warehouse operator</li><li>› Director, MFA</li></ul>
  <p class="txt" style="left:150px;top:494px;font-weight:bold;color:var(--navy)">Neil Carver</p>
  <div class="person" style="left:150px;top:508px;width:34px;height:40px" role="img" aria-label="Portrait of Neil Carver"></div>
  <ul class="txt" style="left:190px;top:508px;width:100px;list-style:none;font-size:7px;line-height:9px"><li>› Transaction adviser</li><li>› Chartered accountant</li><li>› Director, MFA</li></ul>
  <p class="txt" style="left:150px;top:570px;font-weight:bold;color:var(--navy)">Ross Whitlow</p>
  <div class="person" style="left:150px;top:584px;width:34px;height:40px" role="img" aria-label="Portrait of Ross Whitlow"></div>
  <ul class="txt" style="left:190px;top:584px;width:100px;list-style:none;font-size:7px;line-height:9px"><li>› Supply chain strategist</li><li>› Technology lead</li><li>› Director, MFA</li></ul>
  <div class="photo" style="left:360px;top:400px;width:170px;height:110px" role="img" aria-label="Photo of a warehouse interior with stacked goods"></div>
  <div class="brand" style="left:360px;top:540px;gap:7px">
    <div class="brand-mark" style="width:18px;height:18px"></div>
    <div class="brand-name" style="font-size:28px">MFA</div>
    <div class="brand-full" style="font-size:8px;line-height:9px">Meridian<br>Freight<br>Alliance</div>
  </div>
  <p class="contact" style="left:340px;top:600px;width:200px">For further information<br>Contact Graham Pell<br>07 5550 1842<br>0400 555 317<br>info@meridianfreight.example</p>
</section>

</body>
</html>
```